brindle cafe flyer design project

A funky trendy cafe in Melbourne’s CBD that caters too a large range of corporate clients. Located on the door step of a major train station, its a quick turn around cafe for the short time frame customer but also a cafe to sit, relax and enjoy the hustle and bustle from the inside out. We provide All day breakfast, gourmet sandwiches, gourmet rotti wraps, a la carte menu and also heat and serve meals.

BREAKFAST TO GO! ALL BREAKFAST TO GO ITEMS COME WITH A MEDIUM TAKE AWAY COFFEE!
• RAISIN TOAST & COFFEE – $6
• BACON & EGG MUFFIN & COFFEE $7.5
• SPINACH, MUSHROOM OMELETTE MUFFIN & COFFEE $7.5
• OMELETTE WITH CHEESE MUFFIN & COFFEE $7.5
• HAM & CHEESE CROISSANT & COFFEE $7.5
• SWEET OR SAVOURY MUFFIN & COFFEE $6.5
• HAM & CHEESE SANDWICH & COFFEE $8.0
• HAM, CHEESE & TOMATO SANDWICH & COFFEE $8.5

*NOT IN CONJUNCTION WITH BRINDLE CLUB CARD OFFER

WE ALSO HAVE PRE-MADE LUNCH OPTIONS – ASSORTED ROTTI WRAPS (Bbq chicken, honey mustard chicken, pesto chicken & vegetarian) ASSORTED GOURMET SANDWICHES (Mediterranean, Moroccan chicken, Salami, Chicken Schnitzel, Salmon, Brindle & Roast Beef) Soup of the day Pasta of the day Salad of the day

Ph- 03 9517 8836 Fax- 03 9517 8839 Web – www.brindlecafe.com.au 418 KESTREL LANE MELBOURNE 3000

Industry/Entity Type

Cafe

Font styles to use
Serif

Requirements
Must have
• Our 2 branded colours -

PMS 392c
PMS BLACK

```html
<!DOCTYPE html>
<html lang="en">
<head>
<meta charset="utf-8">
<title>Brindle Cafe – Breakfast To Go Flyer</title>
<link href="https://fonts.googleapis.com/css2?family=Bebas+Neue&family=Lato:wght@400;700&display=swap" rel="stylesheet">
<style>
  :root {
    --lime: #bcd42f;
    --lime-dark: #9db420;
    --wood: #4a4139;
    --wood-light: #5a5047;
    --ink: #1f1d1a;
    --white: #ffffff;
    --red: #b5211c;
    --sun-light: #fbeeb0;
    --sun-deep: #f0c955;
    --backdrop: #2b2b2b;
  }
  * { box-sizing: border-box; margin: 0; padding: 0; }
  html, body { width: 806px; height: 1200px; overflow: hidden; background: var(--backdrop); }
  .flyer {
    position: absolute; left: 121px; top: 22px; width: 563px; height: 1155px;
    background: linear-gradient(90deg, var(--wood) 0%, var(--wood-light) 50%, var(--wood) 100%);
    overflow: hidden; font-family: "Lato", sans-serif;
    box-shadow: 0 6px 22px rgba(0,0,0,.5);
  }
  .abs { position: absolute; }
  .top-band { left: 0; top: 0; width: 100%; height: 6px; background: var(--lime); border-bottom: 3px solid var(--white); }
  .photo { background: radial-gradient(ellipse at 50% 50%, #c99a64 0%, #8a4a35 55%, rgba(90,60,40,0) 75%); }
  .photo-top-sandwich { left: 195px; top: 12px; width: 160px; height: 130px; }
  .ribbon { left: 320px; top: 0; width: 213px; height: 150px; }
  .ribbon-text {
    left: 320px; top: 40px; width: 213px; text-align: center;
    font-weight: 700; font-size: 15px; line-height: 19px; color: var(--ink);
  }
  .brand { left: 20px; top: 122px; width: 220px; text-align: center; }
  .brand-mark { width: 70px; height: 70px; border-radius: 50%; background: var(--lime); margin: 0 auto 54px; }
  .brand-name { font-size: 21px; letter-spacing: 3px; color: var(--lime); font-weight: 400; white-space: nowrap; }
  .headline {
    right: 33px; top: 190px; text-align: right; white-space: nowrap;
    font-family: "Bebas Neue", sans-serif; font-weight: 400; font-size: 28px; line-height: 32px; color: var(--white);
  }
  .frame-top { left: 0; top: 322px; width: 563px; height: 20px; background: var(--lime); border-top: 3px solid var(--white); border-bottom: 3px solid var(--white); }
  .photo-benedict {
    left: 0; top: 350px; width: 208px; height: 552px;
    background: linear-gradient(160deg, #f2dc4a 0%, #d9b23a 30%, #3f6b2a 55%, #e8d43c 75%, #c98b5a 100%);
  }
  .divider { left: 208px; top: 342px; width: 27px; height: 565px; background: var(--lime); border-left: 4px solid var(--white); border-right: 4px solid var(--white); }
  .menu-panel {
    left: 235px; top: 345px; width: 328px; height: 555px;
    background:
      repeating-conic-gradient(from 0deg at 55% 45%, rgba(255,255,255,.28) 0deg 6deg, rgba(255,255,255,0) 6deg 14deg),
      radial-gradient(circle at 55% 40%, var(--sun-light) 0%, var(--sun-deep) 85%);
  }
  .disc {
    width: 118px; height: 118px; border-radius: 50%;
    border: 6px solid var(--lime); box-shadow: 0 0 0 3px var(--white);
  }
  .disc-brand { left: 155px; top: 390px; background: radial-gradient(circle, #555 0%, #1a1a1a 90%); }
  .disc-coffee { left: 155px; top: 556px; background: radial-gradient(circle, #e6cba4 0%, #f3f0ea 45%, #1c1c1c 90%); }
  .disc-tarts { left: 155px; top: 720px; background: radial-gradient(circle, #f0b441 0%, #5a3a22 60%, #d8d2c8 95%); }
  .menu { left: 291px; top: 382px; width: 255px; list-style: none; }
  .menu li { display: flex; align-items: center; height: 27px; }
  .item { font-family: "Bebas Neue", sans-serif; font-size: 10px; color: var(--ink); white-space: nowrap; }
  .arrow { flex: 1; height: 10px; margin: 0 6px; }
  .price { font-family: "Bebas Neue", sans-serif; font-size: 21px; color: var(--red); width: 38px; }
  .photo-mid-sandwich { left: 332px; top: 600px; width: 231px; height: 100px; }
  .address { right: 33px; top: 716px; text-align: right; font-family: "Bebas Neue", sans-serif; }
  .street { font-size: 39px; line-height: 36px; color: var(--red); }
  .city { font-size: 28px; line-height: 30px; color: var(--ink); }
  .band-right { left: 290px; top: 830px; width: 273px; height: 22px; background: var(--lime); border-top: 3px solid var(--white); border-bottom: 3px solid var(--white); }
  .band-step { left: 290px; top: 830px; width: 22px; height: 105px; background: var(--lime); border-left: 3px solid var(--white); border-right: 3px solid var(--white); }
  .band-bottom { left: 0; top: 902px; width: 327px; height: 33px; background: var(--lime); border-top: 3px solid var(--white); border-bottom: 3px solid var(--white); }
  .disc-sm { width: 96px; height: 96px; border-radius: 50%; border: 5px solid var(--lime); box-shadow: 0 0 0 3px var(--white); }
  .disc-croissant { left: 312px; top: 803px; background: radial-gradient(circle, #e0a048 0%, #a9642a 70%, #f2ede3 100%); }
  .disc-sandwich { left: 432px; top: 803px; background: radial-gradient(circle, #d8b07a 0%, #8d3a2c 60%, #f2ede3 100%); }
  .lunch { left: 30px; top: 955px; width: 503px; text-align: center; }
  .lunch-title {
    display: flex; align-items: center; justify-content: center; gap: 10px;
    font-family: "Bebas Neue", sans-serif; font-weight: 400; font-size: 30px; color: #e3e33a; line-height: 34px;
  }
  .lunch-title::before, .lunch-title::after { content: ""; width: 42px; height: 2px; background: var(--lime); }
  .lunch-body { margin-top: 8px; font-size: 12.5px; line-height: 18px; color: var(--white); }
  .footer {
    left: 0; top: 1080px; width: 563px; height: 55px; background: var(--lime);
    border-top: 4px solid var(--white); border-bottom: 4px solid var(--white);
    display: flex; align-items: center; justify-content: center; gap: 10px;
    font-weight: 700; font-size: 17px; color: var(--ink);
  }
  .contact { display: flex; align-items: center; gap: 6px; }
  .contact svg { width: 18px; height: 18px; }
</style>
</head>
<body>
<main class="flyer">
  <div class="abs top-band"></div>

  <div class="abs photo photo-top-sandwich" role="img" aria-label="Toasted baguette sandwich with salami"></div>
  <svg class="abs ribbon" viewBox="0 0 213 150" aria-hidden="true">
    <polygon points="0,0 213,0 213,100 106,150 0,100" fill="var(--lime)"/>
  </svg>
  <p class="abs ribbon-text">NOT IN CONJUNCTION<br>WITH BRINDLE CLUB<br>CARD OFFER</p>

  <div class="abs brand">
    <div class="brand-mark"></div>
    <p class="brand-name">BRINDLE CAFE</p>
  </div>

  <h1 class="abs headline">Breakfast to go! All breakfast<br>to go items come with a medium<br>take away coffee!</h1>

  <div class="abs frame-top"></div>
  <div class="abs photo-benedict" role="img" aria-label="Eggs benedict with ham, hollandaise and rocket"></div>
  <div class="abs menu-panel"></div>
  <div class="abs divider"></div>

  <div class="abs disc disc-brand" role="img" aria-label="Coffee roaster sign"></div>
  <div class="abs disc disc-coffee" role="img" aria-label="Cup of latte with latte art"></div>
  <div class="abs disc disc-tarts" role="img" aria-label="Custard tarts and pastries"></div>

  <ul class="abs menu">
    <li><span class="item">Raisin toast &amp; coffee</span><svg class="arrow" viewBox="0 0 100 10" preserveAspectRatio="none"><line x1="0" y1="5" x2="93" y2="5" stroke="var(--lime-dark)" stroke-width="1.6"/><polygon points="92,1 100,5 92,9" fill="var(--lime-dark)"/></svg><span class="price">$6</span></li>
    <li><span class="item">Bacon &amp; egg muffin &amp; coffee</span><svg class="arrow" viewBox="0 0 100 10" preserveAspectRatio="none"><line x1="0" y1="5" x2="93" y2="5" stroke="var(--lime-dark)" stroke-width="1.6"/><polygon points="92,1 100,5 92,9" fill="var(--lime-dark)"/></svg><span class="price">$7.5</span></li>
    <li><span class="item">Spinach, mushroom omelette muffin &amp; coffee</span><svg class="arrow" viewBox="0 0 100 10" preserveAspectRatio="none"><line x1="0" y1="5" x2="93" y2="5" stroke="var(--lime-dark)" stroke-width="1.6"/><polygon points="92,1 100,5 92,9" fill="var(--lime-dark)"/></svg><span class="price">$7.5</span></li>
    <li><span class="item">Omelette with cheese muffin &amp; coffee</span><svg class="arrow" viewBox="0 0 100 10" preserveAspectRatio="none"><line x1="0" y1="5" x2="93" y2="5" stroke="var(--lime-dark)" stroke-width="1.6"/><polygon points="92,1 100,5 92,9" fill="var(--lime-dark)"/></svg><span class="price">$7.5</span></li>
    <li><span class="item">Ham &amp; cheese croissant &amp; coffee</span><svg class="arrow" viewBox="0 0 100 10" preserveAspectRatio="none"><line x1="0" y1="5" x2="93" y2="5" stroke="var(--lime-dark)" stroke-width="1.6"/><polygon points="92,1 100,5 92,9" fill="var(--lime-dark)"/></svg><span class="price">$7.5</span></li>
    <li><span class="item">Sweet or savoury muffin &amp; coffee</span><svg class="arrow" viewBox="0 0 100 10" preserveAspectRatio="none"><line x1="0" y1="5" x2="93" y2="5" stroke="var(--lime-dark)" stroke-width="1.6"/><polygon points="92,1 100,5 92,9" fill="var(--lime-dark)"/></svg><span class="price">$6.5</span></li>
    <li><span class="item">Ham &amp; cheese sandwich &amp; coffee</span><svg class="arrow" viewBox="0 0 100 10" preserveAspectRatio="none"><line x1="0" y1="5" x2="93" y2="5" stroke="var(--lime-dark)" stroke-width="1.6"/><polygon points="92,1 100,5 92,9" fill="var(--lime-dark)"/></svg><span class="price">$8.0</span></li>
    <li><span class="item">Ham, cheese &amp; tomato sandwich &amp; coffee</span><svg class="arrow" viewBox="0 0 100 10" preserveAspectRatio="none"><line x1="0" y1="5" x2="93" y2="5" stroke="var(--lime-dark)" stroke-width="1.6"/><polygon points="92,1 100,5 92,9" fill="var(--lime-dark)"/></svg><span class="price">$8.5</span></li>
  </ul>

  <div class="abs photo photo-mid-sandwich" role="img" aria-label="Two salami baguette sandwiches"></div>

  <div class="abs address">
    <p class="street">418 KESTREL LANE</p>
    <p class="city">MELBOURNE 3000</p>
  </div>

  <div class="abs band-bottom"></div>
  <div class="abs band-step"></div>
  <div class="abs band-right"></div>
  <div class="abs disc-sm disc-croissant" role="img" aria-label="Filled croissants"></div>
  <div class="abs disc-sm disc-sandwich" role="img" aria-label="Baguette sandwich"></div>

  <section class="abs lunch">
    <h2 class="lunch-title">We also have pre-made lunch options</h2>
    <p class="lunch-body">ASSORTED ROTTI WRAPS (Bbq chicken, honey mustard chicken, pesto chicken &amp; vegetarian) ASSORTED GOURMET SANDWICHES (Mediterranean, Moroccan chicken, Salami, Chicken Schnitzel, Salmon, Brindle &amp; Roast Beef) Soup of the day<br>Pasta of the day Salad of the day</p>
  </section>

  <footer class="abs footer">
    <span class="contact"><svg viewBox="0 0 18 18" aria-hidden="true"><rect x="1" y="1" width="16" height="16" rx="3" fill="var(--white)"/><path d="M6 4c-1 1-1 3 1 6s4 4 5 4l1-2-2-1-1 1c-1 0-3-2-3-3l1-1-1-2z" fill="var(--lime)"/></svg>03 9517 8836</span>
    <span class="contact"><svg viewBox="0 0 18 18" aria-hidden="true"><rect x="1" y="1" width="16" height="16" rx="3" fill="var(--white)"/><path d="M6 4c-1 1-1 3 1 6s4 4 5 4l1-2-2-1-1 1c-1 0-3-2-3-3l1-1-1-2z" fill="var(--lime)"/></svg>03 9517 8839</span>
    <span class="contact"><svg viewBox="0 0 18 18" aria-hidden="true"><rect x="1" y="4" width="16" height="11" fill="var(--white)"/><polyline points="1,4 9,10 17,4" fill="none" stroke="var(--lime)" stroke-width="1.4"/></svg>www.brindlecafe.com.au</span>
  </footer>
</main>
</body>
</html>
```